Design für einen Jahresplaner gesucht
Zielgruppe
Scannen und Designen Zahntechnischer und Zahnmedizinischer Arbeiten und das Fräsen und 3d Drucken von bereits in CAD konstruierten Objekten. Wir verfügen über die modernsten Zahntechnischen Technologien und bieten diese als Dienstleister für Dentallabore an.
Aufgabenstellung
Wir benotigen ein Jahresplaner für unsere Kunden. Die Beigefügte Vorlage dient regelrecht nur der Grösenvorlage.
Das Design soll Technisch und Innovativ sein. Gleischzeitig aber gradlinig und nicht zu verspielt.
Das Logo kann ruhig stark ins Auge fallen. Die Schriftfarben sollen überwigen dunkelgrau sein. Hervorzuhebende Bereiche wie z. B. Sonntage, Feiertage sollten die Logofaben beinhalten. Bilder können auch verwendet werden aber wir würden uns über ein Schönes Layout ohne Bilder auch freuen.
PS: Unter dem Logo muss in Feiner Schrift stehen
eine Marke der Norvak GmbH

```html
<!DOCTYPE html>
<html lang="de">
<head>
<meta charset="utf-8">
<title>FRESANO Jahresplaner 2019</title>
<link href="https://fonts.googleapis.com/css2?family=Arimo:wght@400;700&display=swap" rel="stylesheet">
<style>
:root{
  --header:#58585a;
  --white:#ffffff;
  --blue:#1d5f9f;
  --blue-soft:#d7e4f2;
  --week:#6b9bcc;
  --sat:#fcd489;
  --sun:#f5a82a;
  --weekend-text:#d8402a;
  --footer-text:#5a5a5c;
  --wave:#2b8fd4;
  --wave-light:#a9d3f0;
  --accent:#f5a82a;
}
*{margin:0;padding:0;box-sizing:border-box}
html,body{width:1200px;height:840px;overflow:hidden;background:#fff}
body{font-family:"Arimo",Arial,sans-serif}
.sheet{position:relative;width:1200px;height:840px;overflow:hidden;background:var(--white)}
.topbar{position:absolute;left:0;top:0;width:1200px;height:118px;background:var(--header);color:var(--white)}
.brand{position:absolute;left:28px;top:30px}
.brand-row{display:flex;align-items:center;gap:10px}
.brand-dot{width:34px;height:34px;border-radius:50%;background:var(--accent)}
.brand-name{font-size:40px;font-weight:700;letter-spacing:.5px;line-height:1}
.brand-owner{font-size:9.5px;margin:5px 0 0 44px}
.headline{position:absolute;left:358px;top:58px;font-size:21px;font-weight:700;letter-spacing:.3px}
.year{position:absolute;right:26px;top:22px;font-size:74px;font-weight:700;line-height:1}
.months{position:absolute;left:29px;top:133px;display:grid;grid-template-columns:repeat(12,91px);column-gap:5px}
.month h2{font-size:13.5px;font-weight:700;color:var(--blue);height:25px;letter-spacing:.2px}
.month ol{list-style:none}
.month li{position:relative;height:18.9px;margin-bottom:1px;display:flex;align-items:center;padding-left:4px;font-size:7px;color:var(--blue)}
.month li b{font-size:8px;font-weight:700;width:15px}
.month li.o{background:var(--blue-soft)}
.month li.sa{background:var(--sat);color:var(--weekend-text)}
.month li.so{background:var(--sun);color:var(--weekend-text)}
.month li.sa b,.month li.so b{color:var(--blue)}
.month li i{position:absolute;right:4px;top:6px;font-style:normal;font-size:6.5px;color:var(--week)}
.month li small{position:absolute;left:36px;top:8px;font-size:4.6px;color:var(--blue);white-space:nowrap}
.website{position:absolute;left:0;width:1200px;top:788px;text-align:center;font-size:15px;color:var(--footer-text);letter-spacing:.3px}
.wave{position:absolute;left:0;bottom:0;width:1200px;height:60px}
</style>
</head>
<body>
<div class="sheet">
  <header class="topbar">
    <div class="brand">
      <div class="brand-row"><span class="brand-dot"></span><span class="brand-name">FRESANO</span></div>
      <p class="brand-owner">eine Marke der Norvak GmbH</p>
    </div>
    <h1 class="headline">DIGITALE ZAHNMEDIZINISCHE LÖSUNGEN</h1>
    <div class="year">2019</div>
  </header>

  <main class="months">
    <section class="month"><h2>JANUAR</h2><ol>
      <li class="o"><b>01</b>DI<small>Neujahr</small></li><li><b>02</b>MI</li><li class="o"><b>03</b>DO</li><li><b>04</b>FR</li><li class="sa"><b>05</b>SA</li><li class="so"><b>06</b>SO<small>Hl. Drei Könige</small></li>
      <li class="o"><b>07</b>MO<i>02</i></li><li><b>08</b>DI</li><li class="o"><b>09</b>MI</li><li><b>10</b>DO</li><li class="o"><b>11</b>FR</li><li class="sa"><b>12</b>SA</li><li class="so"><b>13</b>SO</li>
      <li><b>14</b>MO<i>03</i></li><li class="o"><b>15</b>DI</li><li><b>16</b>MI</li><li class="o"><b>17</b>DO</li><li><b>18</b>FR</li><li class="sa"><b>19</b>SA</li><li class="so"><b>20</b>SO</li>
      <li class="o"><b>21</b>MO<i>04</i></li><li><b>22</b>DI</li><li class="o"><b>23</b>MI</li><li><b>24</b>DO</li><li class="o"><b>25</b>FR</li><li class="sa"><b>26</b>SA</li><li class="so"><b>27</b>SO</li>
      <li><b>28</b>MO<i>05</i></li><li class="o"><b>29</b>DI</li><li><b>30</b>MI</li><li class="o"><b>31</b>DO</li>
    </ol></section>

    <section class="month"><h2>FEBRUAR</h2><ol>
      <li class="o"><b>01</b>FR</li><li class="sa"><b>02</b>SA</li><li class="so"><b>03</b>SO</li>
      <li><b>04</b>MO<i>06</i></li><li class="o"><b>05</b>DI</li><li><b>06</b>MI</li><li class="o"><b>07</b>DO</li><li><b>08</b>FR</li><li class="sa"><b>09</b>SA</li><li class="so"><b>10</b>SO</li>
      <li class="o"><b>11</b>MO<i>07</i></li><li><b>12</b>DI</li><li class="o"><b>13</b>MI</li><li><b>14</b>DO<small>Valentinstag</small></li><li class="o"><b>15</b>FR</li><li class="sa"><b>16</b>SA</li><li class="so"><b>17</b>SO</li>
      <li><b>18</b>MO<i>08</i></li><li class="o"><b>19</b>DI</li><li><b>20</b>MI</li><li class="o"><b>21</b>DO</li><li><b>22</b>FR</li><li class="sa"><b>23</b>SA</li><li class="so"><b>24</b>SO</li>
      <li class="o"><b>25</b>MO<i>09</i></li><li><b>26</b>DI</li><li class="o"><b>27</b>MI</li><li><b>28</b>DO</li>
    </ol></section>

    <section class="month"><h2>MÄRZ</h2><ol>
      <li class="o"><b>01</b>FR</li><li class="sa"><b>02</b>SA</li><li class="so"><b>03</b>SO</li>
      <li><b>04</b>MO<i>10</i><small>Rosenmontag</small></li><li class="o"><b>05</b>DI<small>Faschingsdienstag</small></li><li><b>06</b>MI<small>Aschermittwoch</small></li><li class="o"><b>07</b>DO</li><li><b>08</b>FR</li><li class="sa"><b>09</b>SA</li><li class="so"><b>10</b>SO</li>
      <li class="o"><b>11</b>MO<i>11</i></li><li><b>12</b>DI</li><li class="o"><b>13</b>MI</li><li><b>14</b>DO</li><li class="o"><b>15</b>FR</li><li class="sa"><b>16</b>SA</li><li class="so"><b>17</b>SO</li>
      <li><b>18</b>MO<i>12</i></li><li class="o"><b>19</b>DI</li><li><b>20</b>MI</li><li class="o"><b>21</b>DO</li><li><b>22</b>FR</li><li class="sa"><b>23</b>SA</li><li class="so"><b>24</b>SO</li>
      <li class="o"><b>25</b>MO<i>13</i></li><li><b>26</b>DI</li><li class="o"><b>27</b>MI</li><li><b>28</b>DO</li><li class="o"><b>29</b>FR</li><li class="sa"><b>30</b>SA</li><li class="so"><b>31</b>SO</li>
    </ol></section>

    <section class="month"><h2>APRIL</h2><ol>
      <li class="o"><b>01</b>MO<i>14</i></li><li><b>02</b>DI</li><li class="o"><b>03</b>MI</li><li><b>04</b>DO</li><li class="o"><b>05</b>FR</li><li class="sa"><b>06</b>SA</li><li class="so"><b>07</b>SO</li>
      <li><b>08</b>MO<i>15</i></li><li class="o"><b>09</b>DI</li><li><b>10</b>MI</li><li class="o"><b>11</b>DO</li><li><b>12</b>FR</li><li class="sa"><b>13</b>SA</li><li class="so"><b>14</b>SO</li>
      <li class="o"><b>15</b>MO<i>16</i></li><li><b>16</b>DI</li><li class="o"><b>17</b>MI</li><li><b>18</b>DO</li><li class="o"><b>19</b>FR<small>Karfreitag</small></li><li class="sa"><b>20</b>SA</li><li class="so"><b>21</b>SO<small>Ostersonntag</small></li>
      <li><b>22</b>MO<i>17</i><small>Ostermontag</small></li><li class="o"><b>23</b>DI</li><li><b>24</b>MI</li><li class="o"><b>25</b>DO</li><li><b>26</b>FR</li><li class="sa"><b>27</b>SA</li><li class="so"><b>28</b>SO</li>
      <li class="o"><b>29</b>MO<i>18</i></li><li><b>30</b>DI</li>
    </ol></section>

    <section class="month"><h2>MAI</h2><ol>
      <li class="o"><b>01</b>MI<small>Tag der Arbeit</small></li><li><b>02</b>DO</li><li class="o"><b>03</b>FR</li><li class="sa"><b>04</b>SA</li><li class="so"><b>05</b>SO</li>
      <li><b>06</b>MO<i>19</i></li><li class="o"><b>07</b>DI</li><li><b>08</b>MI</li><li class="o"><b>09</b>DO</li><li><b>10</b>FR</li><li class="sa"><b>11</b>SA</li><li class="so"><b>12</b>SO</li>
      <li class="o"><b>13</b>MO<i>20</i></li><li><b>14</b>DI</li><li class="o"><b>15</b>MI</li><li><b>16</b>DO</li><li class="o"><b>17</b>FR</li><li class="sa"><b>18</b>SA</li><li class="so"><b>19</b>SO</li>
      <li><b>20</b>MO<i>21</i></li><li class="o"><b>21</b>DI</li><li><b>22</b>MI</li><li class="o"><b>23</b>DO</li><li><b>24</b>FR</li><li class="sa"><b>25</b>SA</li><li class="so"><b>26</b>SO</li>
      <li class="o"><b>27</b>MO<i>22</i></li><li><b>28</b>DI</li><li class="o"><b>29</b>MI</li><li><b>30</b>DO<small>Christi Himmelfahrt</small></li><li class="o"><b>31</b>FR</li>
    </ol></section>

    <section class="month"><h2>JUNI</h2><ol>
      <li class="sa"><b>01</b>SA</li><li class="so"><b>02</b>SO</li>
      <li class="o"><b>03</b>MO<i>23</i></li><li><b>04</b>DI</li><li class="o"><b>05</b>MI</li><li><b>06</b>DO</li><li class="o"><b>07</b>FR</li><li class="sa"><b>08</b>SA</li><li class="so"><b>09</b>SO<small>Pfingstsonntag</small></li>
      <li><b>10</b>MO<i>24</i><small>Pfingstmontag</small></li><li class="o"><b>11</b>DI</li><li><b>12</b>MI</li><li class="o"><b>13</b>DO</li><li><b>14</b>FR</li><li class="sa"><b>15</b>SA</li><li class="so"><b>16</b>SO</li>
      <li class="o"><b>17</b>MO<i>25</i></li><li><b>18</b>DI</li><li class="o"><b>19</b>MI</li><li><b>20</b>DO<small>Fronleichnam</small></li><li class="o"><b>21</b>FR</li><li class="sa"><b>22</b>SA</li><li class="so"><b>23</b>SO</li>
      <li><b>24</b>MO<i>26</i></li><li class="o"><b>25</b>DI</li><li><b>26</b>MI</li><li class="o"><b>27</b>DO</li><li><b>28</b>FR</li><li class="sa"><b>29</b>SA</li><li class="so"><b>30</b>SO</li>
    </ol></section>

    <section class="month"><h2>JULI</h2><ol>
      <li class="o"><b>01</b>MO<i>27</i></li><li><b>02</b>DI</li><li class="o"><b>03</b>MI</li><li><b>04</b>DO</li><li class="o"><b>05</b>FR</li><li class="sa"><b>06</b>SA</li><li class="so"><b>07</b>SO</li>
      <li><b>08</b>MO<i>28</i></li><li class="o"><b>09</b>DI</li><li><b>10</b>MI</li><li class="o"><b>11</b>DO</li><li><b>12</b>FR</li><li class="sa"><b>13</b>SA</li><li class="so"><b>14</b>SO</li>
      <li class="o"><b>15</b>MO<i>29</i></li><li><b>16</b>DI</li><li class="o"><b>17</b>MI</li><li><b>18</b>DO</li><li class="o"><b>19</b>FR</li><li class="sa"><b>20</b>SA</li><li class="so"><b>21</b>SO</li>
      <li><b>22</b>MO<i>30</i></li><li class="o"><b>23</b>DI</li><li><b>24</b>MI</li><li class="o"><b>25</b>DO</li><li><b>26</b>FR</li><li class="sa"><b>27</b>SA</li><li class="so"><b>28</b>SO</li>
      <li class="o"><b>29</b>MO<i>31</i></li><li><b>30</b>DI</li><li class="o"><b>31</b>MI</li>
    </ol></section>

    <section class="month"><h2>AUGUST</h2><ol>
      <li class="o"><b>01</b>DO</li><li><b>02</b>FR</li><li class="sa"><b>03</b>SA</li><li class="so"><b>04</b>SO</li>
      <li class="o"><b>05</b>MO<i>32</i></li><li><b>06</b>DI</li><li class="o"><b>07</b>MI</li><li><b>08</b>DO</li><li class="o"><b>09</b>FR</li><li class="sa"><b>10</b>SA</li><li class="so"><b>11</b>SO</li>
      <li><b>12</b>MO<i>33</i></li><li class="o"><b>13</b>DI</li><li><b>14</b>MI</li><li class="o"><b>15</b>DO<small>Mariä Himmelfahrt</small></li><li><b>16</b>FR</li><li class="sa"><b>17</b>SA</li><li class="so"><b>18</b>SO</li>
      <li class="o"><b>19</b>MO<i>34</i></li><li><b>20</b>DI</li><li class="o"><b>21</b>MI</li><li><b>22</b>DO</li><li class="o"><b>23</b>FR</li><li class="sa"><b>24</b>SA</li><li class="so"><b>25</b>SO</li>
      <li><b>26</b>MO<i>35</i></li><li class="o"><b>27</b>DI</li><li><b>28</b>MI</li><li class="o"><b>29</b>DO</li><li><b>30</b>FR</li><li class="sa"><b>31</b>SA</li>
    </ol></section>

    <section class="month"><h2>SEPTEMBER</h2><ol>
      <li class="so"><b>01</b>SO</li>
      <li><b>02</b>MO<i>36</i></li><li class="o"><b>03</b>DI</li><li><b>04</b>MI</li><li class="o"><b>05</b>DO</li><li><b>06</b>FR</li><li class="sa"><b>07</b>SA</li><li class="so"><b>08</b>SO</li>
      <li class="o"><b>09</b>MO<i>37</i></li><li><b>10</b>DI</li><li class="o"><b>11</b>MI</li><li><b>12</b>DO</li><li class="o"><b>13</b>FR</li><li class="sa"><b>14</b>SA</li><li class="so"><b>15</b>SO</li>
      <li><b>16</b>MO<i>38</i></li><li class="o"><b>17</b>DI</li><li><b>18</b>MI</li><li class="o"><b>19</b>DO</li><li><b>20</b>FR</li><li class="sa"><b>21</b>SA</li><li class="so"><b>22</b>SO</li>
      <li class="o"><b>23</b>MO<i>39</i></li><li><b>24</b>DI</li><li class="o"><b>25</b>MI</li><li><b>26</b>DO</li><li class="o"><b>27</b>FR</li><li class="sa"><b>28</b>SA</li><li class="so"><b>29</b>SO</li>
      <li><b>30</b>MO<i>40</i></li>
    </ol></section>

    <section class="month"><h2>OKTOBER</h2><ol>
      <li class="o"><b>01</b>DI</li><li><b>02</b>MI</li><li class="o"><b>03</b>DO<small>Tag der Dt. Einheit</small></li><li><b>04</b>FR</li><li class="sa"><b>05</b>SA</li><li class="so"><b>06</b>SO</li>
      <li class="o"><b>07</b>MO<i>41</i></li><li><b>08</b>DI</li><li class="o"><b>09</b>MI</li><li><b>10</b>DO</li><li class="o"><b>11</b>FR</li><li class="sa"><b>12</b>SA</li><li class="so"><b>13</b>SO</li>
      <li><b>14</b>MO<i>42</i></li><li class="o"><b>15</b>DI</li><li><b>16</b>MI</li><li class="o"><b>17</b>DO</li><li><b>18</b>FR</li><li class="sa"><b>19</b>SA</li><li class="so"><b>20</b>SO</li>
      <li class="o"><b>21</b>MO<i>43</i></li><li><b>22</b>DI</li><li class="o"><b>23</b>MI</li><li><b>24</b>DO</li><li class="o"><b>25</b>FR</li><li class="sa"><b>26</b>SA</li><li class="so"><b>27</b>SO</li>
      <li><b>28</b>MO<i>44</i></li><li class="o"><b>29</b>DI</li><li><b>30</b>MI</li><li class="o"><b>31</b>DO<small>Reformationstag</small></li>
    </ol></section>

    <section class="month"><h2>NOVEMBER</h2><ol>
      <li class="o"><b>01</b>FR<small>Allerheiligen</small></li><li class="sa"><b>02</b>SA</li><li class="so"><b>03</b>SO</li>
      <li><b>04</b>MO<i>45</i></li><li class="o"><b>05</b>DI</li><li><b>06</b>MI</li><li class="o"><b>07</b>DO</li><li><b>08</b>FR</li><li class="sa"><b>09</b>SA</li><li class="so"><b>10</b>SO</li>
      <li class="o"><b>11</b>MO<i>46</i></li><li><b>12</b>DI</li><li class="o"><b>13</b>MI</li><li><b>14</b>DO</li><li class="o"><b>15</b>FR</li><li class="sa"><b>16</b>SA</li><li class="so"><b>17</b>SO</li>
      <li><b>18</b>MO<i>47</i></li><li class="o"><b>19</b>DI</li><li><b>20</b>MI<small>Buß- und Bettag</small></li><li class="o"><b>21</b>DO</li><li><b>22</b>FR</li><li class="sa"><b>23</b>SA</li><li class="so"><b>24</b>SO</li>
      <li class="o"><b>25</b>MO<i>48</i></li><li><b>26</b>DI</li><li class="o"><b>27</b>MI</li><li><b>28</b>DO</li><li class="o"><b>29</b>FR</li><li class="sa"><b>30</b>SA</li>
    </ol></section>

    <section class="month"><h2>DEZEMBER</h2><ol>
      <li class="so"><b>01</b>SO</li>
      <li><b>02</b>MO<i>49</i></li><li class="o"><b>03</b>DI</li><li><b>04</b>MI</li><li class="o"><b>05</b>DO</li><li><b>06</b>FR</li><li class="sa"><b>07</b>SA</li><li class="so"><b>08</b>SO</li>
      <li class="o"><b>09</b>MO<i>50</i></li><li><b>10</b>DI</li><li class="o"><b>11</b>MI</li><li><b>12</b>DO</li><li class="o"><b>13</b>FR</li><li class="sa"><b>14</b>SA</li><li class="so"><b>15</b>SO</li>
      <li><b>16</b>MO<i>51</i></li><li class="o"><b>17</b>DI</li><li><b>18</b>MI</li><li class="o"><b>19</b>DO</li><li><b>20</b>FR</li><li class="sa"><b>21</b>SA</li><li class="so"><b>22</b>SO</li>
      <li class="o"><b>23</b>MO<i>52</i></li><li><b>24</b>DI<small>Heiligabend</small></li><li class="o"><b>25</b>MI<small>1. Weihnachtstag</small></li><li><b>26</b>DO<small>2. Weihnachtstag</small></li><li class="o"><b>27</b>FR</li><li class="sa"><b>28</b>SA</li><li class="so"><b>29</b>SO</li>
      <li><b>30</b>MO<i>01</i></li><li class="o"><b>31</b>DI<small>Silvester</small></li>
    </ol></section>
  </main>

  <p class="website">www.fresano.de</p>
  <svg class="wave" viewBox="0 0 1200 60" preserveAspectRatio="none" aria-hidden="true">
    <path d="M0 14 C 300 30, 700 56, 1200 58 L1200 60 L0 60 Z" fill="var(--wave-light)"/>
    <path d="M0 22 C 300 40, 650 58, 1000 60 L0 60 Z" fill="var(--wave)"/>
  </svg>
</div>
</body>
</html>
```